New Company Newsletter Template Needed!!!

We need some new graphics/design for us to create our company newsletter in MS Publisher/Word. Prefer simple, modern design that can be easy to update each month, flexible for adding images and include our company logo (attached).
Also attached our basic existing template but we do not want to use the same “swoosh” ribbon and want to reduce the number of colours used.
Needs to be elements we can move into the software and create a PDF newsletter to circulate.

Font styles to use
Sans Serif

Requirements
Must have
• Company logo
Nice to have
• If any colours should fit into our company logo palette

```html
<!DOCTYPE html>
<html lang="en">
<head>
<meta charset="utf-8">
<title>Company Newsletter Template – Four Page Layouts</title>
<link rel="stylesheet" href="https://fonts.googleapis.com/css2?family=Montserrat:wght@600;700;800&family=Open+Sans:wght@400;600&display=swap">
<style>
  :root {
    --canvas: #000000;
    --paper: #ffffff;
    --crimson: #c8173f;
    --magenta: #9c1056;
    --red: #e2263a;
    --orange: #f26a1b;
    --amber: #f7a81b;
    --yellow: #ffd23c;
    --navy: #0c2a7a;
    --blue-head: #1f45a8;
    --title-red: #d3173f;
    --ink: #3b3b3b;
    --placeholder: #e3e3e3;
    --placeholder-ink: #555555;
    --sidebar-tint: #f4f6fb;
    --muted: #9a9a9a;
  }
  * { box-sizing: border-box; margin: 0; padding: 0; }
  html, body { width: 902px; height: 1200px; overflow: hidden; background: var(--canvas); }
  .sheet-set { position: relative; width: 902px; height: 1200px; }
  .page {
    position: absolute; width: 433px; height: 578px; background: var(--paper);
    overflow: hidden; font-family: "Open Sans", Arial, sans-serif; color: var(--ink);
  }
  .page--cover-red { left: 11px; top: 6px; }
  .page--cover-navy { left: 458px; top: 6px; }
  .page--inner-feature { left: 11px; top: 604px; }
  .page--inner-story { left: 458px; top: 604px; }

  .wave { position: absolute; left: 0; width: 433px; display: block; }
  .wave--head { top: 0; height: 118px; }
  .wave--head-short { top: 0; height: 82px; }
  .wave--foot { top: 498px; height: 60px; }

  .masthead-title {
    position: absolute; left: 10px; top: 20px; font-family: "Montserrat", Arial, sans-serif;
    font-weight: 800; font-size: 31px; letter-spacing: 0.5px; color: var(--paper);
  }
  .masthead-meta {
    position: absolute; left: 12px; top: 60px; font-family: "Montserrat", Arial, sans-serif;
    font-weight: 600; font-style: italic; font-size: 5.6px; color: var(--paper); word-spacing: 1px;
  }
  .masthead-meta span { margin-right: 14px; }

  .brand { position: absolute; display: flex; align-items: center; gap: 6px;
    font-family: "Montserrat", Arial, sans-serif; font-weight: 600; color: var(--paper); font-size: 22px; }
  .brand-dot { width: 22px; height: 22px; border-radius: 50%; background: var(--amber); }
  .brand--right { left: 280px; top: 24px; }
  .brand--left { left: 16px; top: 12px; }

  .sidebar-tint { position: absolute; left: 0; top: 138px; width: 150px; height: 410px; background: var(--sidebar-tint); }
  .contents-bar {
    position: absolute; left: 0; top: 138px; width: 150px; height: 25px;
    font-family: "Montserrat", Arial, sans-serif; font-weight: 700; font-size: 11px; color: var(--paper);
    display: flex; align-items: center; justify-content: center;
  }
  .contents-bar--red { background: var(--crimson); }
  .contents-bar--navy { background: var(--navy); }
  .contents-list { position: absolute; left: 20px; top: 172px; list-style: none; font-size: 7.6px; }
  .contents-list li { height: 14.6px; line-height: 14.6px; }
  .contents-list li::before { content: "•"; font-size: 6px; margin-right: 5px; position: relative; top: -1px; }

  .image-slot {
    position: absolute; background: var(--placeholder); color: var(--placeholder-ink);
    font-size: 8.6px; letter-spacing: 0.3px; display: flex; align-items: center; justify-content: center;
  }
  .lead-headline {
    position: absolute; font-family: "Montserrat", Arial, sans-serif; font-weight: 700;
    font-size: 17.5px; color: var(--blue-head); white-space: nowrap;
  }
  .para-title {
    position: absolute; font-family: "Montserrat", Arial, sans-serif; font-weight: 700;
    font-size: 10.4px; color: var(--title-red); line-height: 1.25;
  }
  .copy { position: absolute; font-size: 6.1px; line-height: 1.62; }
  .copy p + p { margin-top: 8px; }
  .copy--light { color: var(--paper); }
  .feature-box { position: absolute; left: 6px; top: 214px; width: 148px; height: 286px; background: var(--crimson); }
  .feature-box .para-title { color: var(--paper); left: 12px; top: 12px; }
  .copyright { position: absolute; right: 9px; top: 562px; font-size: 8px; color: var(--muted); letter-spacing: 0.3px; }
</style>
</head>
<body>
<svg width="0" height="0" style="position:absolute" aria-hidden="true">
  <defs>
    <linearGradient id="warmSweep" x1="0" y1="0" x2="1" y2="0">
      <stop offset="0" stop-color="#d81f45"/>
      <stop offset="0.55" stop-color="#e83a2e"/>
      <stop offset="1" stop-color="#f5821f"/>
    </linearGradient>
    <linearGradient id="goldSweep" x1="0" y1="0" x2="1" y2="0">
      <stop offset="0" stop-color="#f26a1b"/>
      <stop offset="0.6" stop-color="#f7a81b"/>
      <stop offset="1" stop-color="#ffd23c"/>
    </linearGradient>
    <linearGradient id="berrySweep" x1="0" y1="0" x2="1" y2="0">
      <stop offset="0" stop-color="#8a0e4f"/>
      <stop offset="1" stop-color="#d81f45"/>
    </linearGradient>
  </defs>
</svg>

<main class="sheet-set">

  <!-- Cover layout, red contents bar -->
  <section class="page page--cover-red">
    <svg class="wave wave--head" viewBox="0 0 433 118" preserveAspectRatio="none" aria-hidden="true">
      <path d="M0 0H433V72C360 60 290 112 200 104C120 98 60 84 0 96Z" fill="url(#warmSweep)"/>
      <path d="M0 96C60 84 120 98 200 104C290 112 360 60 433 72V80C360 70 290 118 200 112C120 106 60 92 0 102Z" fill="url(#goldSweep)"/>
      <path d="M200 112C290 118 360 70 433 80V86C360 78 300 116 210 116Z" fill="url(#berrySweep)"/>
    </svg>
    <h1 class="masthead-title">NEWSLETTER</h1>
    <div class="masthead-meta"><span>January 2030</span><span>Issue #45</span><span>Company Important Info Goes here</span></div>
    <div class="brand brand--right"><span class="brand-dot"></span>Brightway</div>

    <div class="sidebar-tint"></div>
    <div class="contents-bar contents-bar--red">Inside this Issue:</div>
    <ul class="contents-list">
      <li>Inside Story Title 2</li><li>Inside Story Title 2</li><li>Inside Story Title 3</li><li>Inside Story Title 3</li>
      <li>Inside Story Title 4</li><li>Inside Story Title 4</li><li>Inside Story Title 2</li><li>Inside Story Title 2</li>
      <li>Inside Story Title 3</li><li>Inside Story Title 3</li><li>Inside Story Title 4</li><li>Inside Story Title 4</li>
    </ul>
    <h3 class="para-title" style="left:17px;top:366px">Parragraph Title here</h3>
    <div class="copy" style="left:17px;top:382px;width:128px">
      <p>This story can fit 125-165 words. This is greeked text for copy placement. Use this as a placeholder for text when it's not readily available. This is a layout tool intended to aid in the design process, to provide adequate amounts of copy to proof a layout and style. It's a necessary element for building good design. Greeked copy is a standard in the marketing industry.</p>
      <p>The process of This story can fit 125-165 words. This is greeked text for copy placement. The process of This story can fit 125-165 words. This is greeked text for copy placement.</p>
    </div>

    <div class="image-slot" role="img" aria-label="Lead story photo" style="left:165px;top:132px;width:252px;height:134px">IMAGE HERE</div>
    <h2 class="lead-headline" style="left:165px;top:268px">Lead Story Headline</h2>
    <div class="copy" style="left:166px;top:294px;width:262px">
      <p>This story can fit 125-165 words. This is greeked text for copy placement. Use this as a placeholder for text when it's not readily available. This is a layout tool intended to aid in the design process, to provide adequate amounts of copy to proof a layout and style. It's a necessary element for building good design. Greeked copy is a standard in the marketing industry.</p>
      <p>The process of This story can fit 125-165 words. This is greeked text for copy placement. Use this as a placeholder for text when it's not readily available. This is a layout tool intended to aid in the design process, to provide adequate amounts of copy to proof a layout and style. It's a necessary element for building good design. Greeked copy is a standard in the marketing industry.</p>
      <p>The process of This story can fit 125-165 words. This is greeked text for copy placement. Use this as a placeholder for text when it's not readily available. This is a layout tool intended to aid in the design process, to provide adequate amounts of copy to proof a layout and style. The process of This story can fit 125-165 words. This is greeked text for copy placement.</p>
    </div>

    <svg class="wave wave--foot" viewBox="0 0 433 60" preserveAspectRatio="none" aria-hidden="true">
      <path d="M0 44C120 40 260 20 433 0V28C300 44 160 56 0 56Z" fill="url(#berrySweep)"/>
      <path d="M0 56C160 56 300 44 433 28V36C300 52 160 60 0 60Z" fill="url(#goldSweep)"/>
    </svg>
    <p class="copyright">Copyright text here</p>
  </section>

  <!-- Cover layout, navy contents bar -->
  <section class="page page--cover-navy">
    <svg class="wave wave--head" viewBox="0 0 433 118" preserveAspectRatio="none" aria-hidden="true">
      <path d="M0 0H433V72C360 60 290 112 200 104C120 98 60 84 0 96Z" fill="url(#warmSweep)"/>
      <path d="M0 96C60 84 120 98 200 104C290 112 360 60 433 72V80C360 70 290 118 200 112C120 106 60 92 0 102Z" fill="url(#goldSweep)"/>
      <path d="M200 112C290 118 360 70 433 80V86C360 78 300 116 210 116Z" fill="url(#berrySweep)"/>
    </svg>
    <h1 class="masthead-title">NEWSLETTER</h1>
    <div class="masthead-meta"><span>January 2030</span><span>Issue #45</span><span>Company Important Info Goes here</span></div>
    <div class="brand brand--right"><span class="brand-dot"></span>Brightway</div>

    <div class="sidebar-tint"></div>
    <div class="contents-bar contents-bar--navy">Inside this Issue:</div>
    <ul class="contents-list">
      <li>Inside Story Title 2</li><li>Inside Story Title 2</li><li>Inside Story Title 3</li><li>Inside Story Title 3</li>
      <li>Inside Story Title 4</li><li>Inside Story Title 4</li><li>Inside Story Title 2</li><li>Inside Story Title 2</li>
      <li>Inside Story Title 3</li><li>Inside Story Title 3</li><li>Inside Story Title 4</li><li>Inside Story Title 4</li>
    </ul>
    <h3 class="para-title" style="left:17px;top:366px;color:var(--navy)">Paragraph Title here</h3>
    <div class="copy" style="left:17px;top:382px;width:128px">
      <p>This story can fit 125-165 words. This is greeked text for copy placement. Use this as a placeholder for text when it's not readily available. This is a layout tool intended to aid in the design process, to provide adequate amounts of copy to proof a layout and style. It's a necessary element for building good design. Greeked copy is a standard in the marketing industry.</p>
      <p>The process of This story can fit 125-165 words. This is greeked text for copy placement. The process of This story can fit 125-165 words. This is greeked text for copy placement.</p>
    </div>

    <div class="image-slot" role="img" aria-label="Lead story photo" style="left:165px;top:132px;width:252px;height:134px">IMAGE HERE</div>
    <h2 class="lead-headline" style="left:165px;top:268px">Lead Story Headline</h2>
    <div class="copy" style="left:166px;top:294px;width:262px">
      <p>This story can fit 125-165 words. This is greeked text for copy placement. Use this as a placeholder for text when it's not readily available. This is a layout tool intended to aid in the design process, to provide adequate amounts of copy to proof a layout and style. It's a necessary element for building good design. Greeked copy is a standard in the marketing industry.</p>
      <p>The process of This story can fit 125-165 words. This is greeked text for copy placement. Use this as a placeholder for text when it's not readily available. This is a layout tool intended to aid in the design process, to provide adequate amounts of copy to proof a layout and style. It's a necessary element for building good design. Greeked copy is a standard in the marketing industry.</p>
      <p>The process of This story can fit 125-165 words. This is greeked text for copy placement. Use this as a placeholder for text when it's not readily available. This is a layout tool intended to aid in the design process, to provide adequate amounts of copy to proof a layout and style. The process of This story can fit 125-165 words. This is greeked text for copy placement.</p>
    </div>

    <svg class="wave wave--foot" viewBox="0 0 433 60" preserveAspectRatio="none" aria-hidden="true">
      <path d="M0 44C120 40 260 20 433 0V28C300 44 160 56 0 56Z" fill="url(#berrySweep)"/>
      <path d="M0 56C160 56 300 44 433 28V36C300 52 160 60 0 60Z" fill="url(#goldSweep)"/>
    </svg>
    <p class="copyright">Copyright text here</p>
  </section>

  <!-- Inner layout with feature box -->
  <section class="page page--inner-feature">
    <svg class="wave wave--head-short" viewBox="0 0 433 82" preserveAspectRatio="none" aria-hidden="true">
      <path d="M0 0H433V38C360 30 300 72 210 68C130 64 60 50 0 58Z" fill="url(#warmSweep)"/>
      <path d="M0 58C60 50 130 64 210 68C300 72 360 30 433 38V46C360 38 300 80 210 76C130 72 60 58 0 66Z" fill="url(#goldSweep)"/>
      <path d="M210 76C300 80 360 38 433 46V52C360 46 300 82 220 80Z" fill="url(#berrySweep)"/>
    </svg>
    <div class="brand brand--left"><span class="brand-dot"></span>Brightway</div>

    <div class="image-slot" role="img" aria-label="Feature photo" style="left:6px;top:86px;width:148px;height:126px">IMAGE HERE</div>
    <div class="feature-box">
      <h3 class="para-title">Parragraph Title here</h3>
      <div class="copy copy--light" style="left:12px;top:28px;width:128px">
        <p>This story can fit 125-165 words. This is greeked text for copy placement. Use this as a placeholder for text when it's not readily available. This is a layout tool intended to aid in the design process, to provide adequate amounts of copy to proof a layout and style. It's a necessary element for building good design. Greeked copy is a standard in the marketing industry.</p>
        <p>The process of This story can fit 125-165 words. This is greeked text for copy placement. The process of This story can fit 125-165 words. This is greeked text for copy placement. Use this as a placeholder for text when it's not readily available. This is a layout tool intended to aid in the design process, to provide adequate amounts of copy to proof a layout and style. It's a necessary element for building good design. Greeked copy is a standard in the marketing industry. The process of leadership.</p>
      </div>
    </div>

    <h2 class="lead-headline" style="left:164px;top:100px">Lead Story Headline</h2>
    <div class="copy" style="left:165px;top:124px;width:128px">
      <p>This story can fit 125-165 words. This is greeked text for copy placement. Use this as a placeholder for text when it's not readily available. This is a layout tool intended to aid in the design process, to provide adequate amounts of copy to proof a layout and style. It's a necessary element for building good design. Greeked copy is a standard in the marketing industry.</p>
      <p>The process of This story can fit 125-165 words. This is greeked text for copy placement. Use this as a placeholder for text when it's not readily available. This is a layout tool intended to aid in the design process, to provide adequate amounts of copy to proof a layout and style. It's a necessary element for building good design. Greeked copy is a standard in the marketing industry.</p>
    </div>
    <div class="copy" style="left:299px;top:124px;width:128px">
      <p>This story can fit 125-165 words. This is greeked text for copy placement. Use this as a placeholder for text when it's not readily available. This is a layout tool intended to aid in the design process, to provide adequate amounts of copy to proof a layout and style. It's a necessary element for building good design. Greeked copy is a standard in the marketing industry.</p>
      <p>The process of This story can fit 125-165 words. This is greeked text for copy placement. Use this as a placeholder for text when it's not readily available. This is a layout tool intended to aid in the design process, to provide adequate amounts of copy to proof a layout and style. It's a necessary element for building good design. Greeked copy is a standard in the marketing industry.</p>
    </div>
    <div class="image-slot" role="img" aria-label="Secondary story photo" style="left:164px;top:343px;width:259px;height:157px">IMAGE HERE</div>

    <svg class="wave wave--foot" viewBox="0 0 433 60" preserveAspectRatio="none" aria-hidden="true">
      <path d="M0 44C120 40 260 20 433 0V28C300 44 160 56 0 56Z" fill="url(#berrySweep)"/>
      <path d="M0 56C160 56 300 44 433 28V36C300 52 160 60 0 60Z" fill="url(#goldSweep)"/>
    </svg>
    <p class="copyright">Copyright text here</p>
  </section>

  <!-- Inner layout with side story -->
  <section class="page page--inner-story">
    <svg class="wave wave--head-short" viewBox="0 0 433 82" preserveAspectRatio="none" aria-hidden="true">
      <path d="M0 0H433V38C360 30 300 72 210 68C130 64 60 50 0 58Z" fill="url(#warmSweep)"/>
      <path d="M0 58C60 50 130 64 210 68C300 72 360 30 433 38V46C360 38 300 80 210 76C130 72 60 58 0 66Z" fill="url(#goldSweep)"/>
      <path d="M210 76C300 80 360 38 433 46V52C360 46 300 82 220 80Z" fill="url(#berrySweep)"/>
    </svg>
    <div class="brand brand--left"><span class="brand-dot"></span>Brightway</div>

    <div class="image-slot" role="img" aria-label="Lead story photo" style="left:6px;top:86px;width:258px;height:134px">IMAGE HERE</div>
    <h2 class="lead-headline" style="left:13px;top:226px">Lead Story Headline</h2>
    <div class="copy" style="left:13px;top:252px;width:124px">
      <p>This story can fit 125-165 words. This is greeked text for copy placement. Use this as a placeholder for text when it's not readily available. This is a layout tool intended to aid in the design process, to provide adequate amounts of copy to proof a layout and style. It's a necessary element for building good design. Greeked copy is a standard in the marketing industry.</p>
      <p>The process of This story can fit 125-165 words. This is greeked text for copy placement. Use this as a placeholder for text when it's not readily available. This is a layout tool intended to aid in the design process, to provide adequate amounts of copy to proof a layout and style. It's a necessary element for building good design. Greeked copy is a standard in the marketing industry.</p>
      <p>The process of This story can fit 125-165 words. This is greeked text for copy placement. Use this as a placeholder for text when it's not readily available.</p>
    </div>
    <div class="copy" style="left:144px;top:252px;width:124px">
      <p>This story can fit 125-165 words. This is greeked text for copy placement. Use this as a placeholder for text when it's not readily available. This is a layout tool intended to aid in the design process, to provide adequate amounts of copy to proof a layout and style. It's a necessary element for building good design. Greeked copy is a standard in the marketing industry.</p>
      <p>The process of This story can fit 125-165 words. This is greeked text for copy placement. Use this as a placeholder for text when it's not readily available. This is a layout tool intended to aid in the design process, to provide adequate amounts of copy to proof a layout and style. It's a necessary element for building good design. The process of This story can fit 125-165 words.</p>
    </div>

    <h3 class="para-title" style="left:280px;top:82px;font-size:13.6px">2 Line Paragraph<br>Title here</h3>
    <div class="copy" style="left:280px;top:124px;width:146px">
      <p>This story can fit 125-165 words. This is greeked text for copy placement. Use this as a placeholder for text when it's not readily available. This is a layout tool intended to aid in the design process, to provide adequate amounts of copy to proof a layout and style. It's a necessary element for building good design. Greeked copy is a standard in the marketing industry.</p>
      <p>The process of This story can fit 125-165 words. This is greeked text for copy placement. Use this as a placeholder for text when it's not readily available. This is a layout tool intended to aid in the design process, to provide adequate amounts of copy to proof a layout and style. It's a necessary element for building good design. Greeked copy is a standard in the marketing industry.</p>
      <p>The process of This story can fit 125-165 words. This is greeked text for copy placement. Use this as a placeholder for text when it's not readily available. This is a layout tool intended to aid in the design process.</p>
    </div>

    <svg class="wave wave--foot" viewBox="0 0 433 60" preserveAspectRatio="none" aria-hidden="true">
      <path d="M0 44C120 40 260 20 433 0V28C300 44 160 56 0 56Z" fill="url(#berrySweep)"/>
      <path d="M0 56C160 56 300 44 433 28V36C300 52 160 60 0 60Z" fill="url(#goldSweep)"/>
    </svg>
    <p class="copyright">Copyright text here</p>
  </section>

</main>
</body>
</html>
```